Pim Tavel Brochure Design

We are a Marketing company offering different services. Services must be outlined on design we will provive text for the services once project is accepted.

Service Titles to include in design

Corporate Branding
Marketing
Web Design 
Business Consultation
Printing
Mailing
Automation
Pim Tavel Choice

Please post designs, we have n

Target Market(s)

18+ Years Old

Must have
• Web 2.0 Graphics
• Eye catching design
Nice to have
• Rich Graphics
• Creativity
Should not have
• Standard Templates
• Only bullets

```html
<!DOCTYPE html>
<html lang="en">
<head>
<meta charset="utf-8">
<title>Pim Tavel Marketing – Brochure Outside</title>
<link rel="stylesheet" href="https://fonts.googleapis.com/css2?family=PT+Sans:wght@400;700&family=Montserrat:wght@500;600&display=swap">
<style>
  :root {
    --bg-dark: #333333;
    --bg-mid: #3c3c3c;
    --text-light: #ffffff;
    --text-dark: #2e2e2e;
    --brand-orange: #f5a623;
    --orange-deep: #e88600;
    --orange-light: #fbb540;
    --steel-light: #cfcdc9;
    --steel-warm: #c9a36d;
  }
  * { margin: 0; padding: 0; box-sizing: border-box; }
  html, body { width: 1200px; height: 932px; overflow: hidden; background: var(--bg-dark); }
  .brochure {
    position: relative;
    width: 1200px;
    height: 932px;
    overflow: hidden;
    background: radial-gradient(ellipse at 70% 20%, var(--bg-mid), var(--bg-dark) 70%);
    font-family: "PT Sans", sans-serif;
    color: var(--text-light);
  }
  .gear-art { position: absolute; inset: 0; width: 1200px; height: 932px; }
  .about {
    position: absolute;
    left: 31px;
    top: 112px;
    width: 340px;
    text-align: center;
  }
  .about__title { font-size: 25px; font-weight: 400; line-height: 1.05; }
  .about__text { font-size: 16.5px; line-height: 18px; margin-bottom: 18px; }
  .contact {
    position: absolute;
    left: 20px;
    top: 534px;
    width: 355px;
    text-align: center;
    font-style: normal;
  }
  .contact__name { font-size: 26px; font-weight: 400; line-height: 1.2; margin-bottom: 14px; }
  .contact__address, .contact__phones { font-size: 19.5px; line-height: 18px; }
  .contact__address { margin-bottom: 18px; }
  .contact__phones { margin-bottom: 18px; }
  .contact__email { font-size: 20px; line-height: 24px; margin-bottom: 12px; }
  .contact__web { font-size: 21.5px; line-height: 24px; }
  .brand {
    position: absolute;
    right: 36px;
    top: 58px;
    display: flex;
    align-items: center;
    gap: 12px;
  }
  .brand__dot { width: 22px; height: 22px; border-radius: 50%; background: var(--brand-orange); }
  .brand__name {
    font-weight: 400;
    font-size: 30px;
    line-height: 1;
    color: var(--brand-orange);
    letter-spacing: 1px;
  }
  .services {
    position: absolute;
    left: 476px;
    top: 520px;
    width: 340px;
    text-align: center;
    list-style: none;
    color: var(--text-dark);
  }
  .services__title {
    font-family: "Montserrat", sans-serif;
    font-weight: 600;
    font-size: 15px;
    letter-spacing: 3px;
    margin-bottom: 10px;
  }
  .services__item {
    font-size: 20px;
    font-weight: 700;
    line-height: 28px;
  }
  .tagline {
    position: absolute;
    right: 25px;
    top: 807px;
    font-family: "Montserrat", sans-serif;
    font-weight: 500;
    font-size: 19px;
    letter-spacing: 3.4px;
    color: var(--text-light);
  }
</style>
</head>
<body>
<main class="brochure">
  <svg class="gear-art" viewBox="0 0 1200 932" role="img" aria-label="Two interlocking gears, a large orange gear at right and a steel-to-orange gear at centre">
    <defs>
      <linearGradient id="gear-orange" x1="0" y1="0" x2="0" y2="1">
        <stop offset="0" stop-color="#fbb540"/>
        <stop offset="1" stop-color="#e88600"/>
      </linearGradient>
      <linearGradient id="gear-steel" x1="0" y1="0" x2="0" y2="1">
        <stop offset="0" stop-color="#cfcdc9"/>
        <stop offset="0.5" stop-color="#c9a36d"/>
        <stop offset="1" stop-color="#e88600"/>
      </linearGradient>
    </defs>
    <circle cx="1132" cy="437" r="290" fill="url(#gear-orange)"/>
    <circle cx="646" cy="650" r="275" fill="url(#gear-steel)"/>
  </svg>

  <section class="about">
    <h2 class="about__title">ABOUT US</h2>
    <p class="about__text">Lorem ipsum dolor sit amet, consectetuer adipiscing elit. Nullam euismod mollis nisl. Morbi ultricies neque vel ipsum. Aenean cursus. Aenean elit. Aliquam commodo. Praesent quis ante in eros gravida blandit. Nullam sagittis. Ut eu urna in orci gravida sodales. Sed volutpat cursus nunc. Mauris porta dolor quis lectus tincidunt congue. Mauris sed arcu id erat molestie laoreet.</p>
    <p class="about__text">Lorem ipsum dolor sit amet, consectetuer adipiscing elit. Nullam euismod mollis nisl. Morbi ultricies neque vel ipsum. Aenean cursus. Aenean elit. Aliquam commodo. Praesent quis ante in eros gravida blandit. Nullam sagittis. Ut eu urna in orci gravida sodales. Sed volutpat cursus nunc. Mauris porta dolor quis lectus tincidunt congue. Mauris sed arcu id erat molestie laoreet.</p>
  </section>

  <address class="contact">
    <h2 class="contact__name">PIM TAVEL MARKETING</h2>
    <p class="contact__address">1234 Anywhere Lane<br>Suite 101<br>City, State, Zip Code<br>Country</p>
    <p class="contact__phones">Phone: 555-555-5555<br>Fax: 555-555-5556<br>Toll-Free: 800-555-5555</p>
    <p class="contact__email">email@pimtavelmarketing.com</p>
    <p class="contact__web">www.pimtavelmarketing.com</p>
  </address>

  <div class="brand">
    <span class="brand__dot"></span>
    <span class="brand__name">PIM TAVEL MARKETING</span>
  </div>

  <ul class="services">
    <li class="services__title">OUR SERVICES</li>
    <li class="services__item">Corporate Branding</li>
    <li class="services__item">Marketing</li>
    <li class="services__item">Web Design</li>
    <li class="services__item">Business Consultation</li>
    <li class="services__item">Printing</li>
    <li class="services__item">Mailing</li>
    <li class="services__item">Automation</li>
    <li class="services__item">Pim Tavel Choice</li>
  </ul>

  <p class="tagline">MARKETING THAT WORKS!</p>
</main>
</body>
</html>
```